Corvana Wound Care Business card design

We need a business card designed around our logo which was provided. The logo of preference is the colored. Also the colors and fonts were provided.

Target Market(s)

Our Referral partners are home health agencies.

Industry/Entity Type

Healthcare

Contact Information for Business Card

Name , Phone #, Email , Title

Requirements
Nice to have
• Creativity
Should not have
• basic

```html
<!DOCTYPE html>
<html lang="en">
<head>
<meta charset="utf-8">
<title>Corvana Wound Care – Business Card</title>
<link rel="stylesheet" href="https://fonts.googleapis.com/css2?family=Archivo:wght@500;600;700&display=swap">
<style>
  :root {
    --navy: #2b3990;
    --deep-blue: #1f4fa8;
    --cyan: #00aeef;
    --ink: #1c3f8f;
    --white: #ffffff;
    --backdrop: #e9ebef;
    --card-w: 515px;
    --card-h: 296px;
  }
  * { margin: 0; padding: 0; box-sizing: border-box; }
  html, body {
    width: 1200px;
    height: 900px;
    overflow: hidden;
    background: var(--backdrop);
    font-family: "Archivo", "Helvetica Neue", Arial, sans-serif;
  }
  .canvas {
    position: relative;
    width: 1200px;
    height: 900px;
  }
  .card {
    position: absolute;
    top: 302px;
    width: var(--card-w);
    height: var(--card-h);
    box-shadow: 0 4px 10px rgba(0, 0, 0, 0.25);
    overflow: hidden;
  }
  .card--front {
    left: 72px;
    background: linear-gradient(60deg, var(--navy) 0%, var(--deep-blue) 40%, var(--cyan) 100%);
  }
  .card--back {
    left: 615px;
    background: var(--white);
  }

  /* front */
  .front-brand {
    position: absolute;
    left: 150px;
    top: 130px;
    display: flex;
    align-items: center;
    gap: 12px;
    color: var(--white);
  }
  .front-brand__dot {
    width: 30px;
    height: 30px;
    border-radius: 50%;
    background: var(--white);
  }
  .front-brand__name {
    font-weight: 600;
    font-size: 26px;
    letter-spacing: 0.2px;
    line-height: 1.1;
  }

  /* back */
  .back-brand {
    position: absolute;
    left: 46px;
    top: 46px;
    display: flex;
    align-items: center;
    gap: 9px;
    color: var(--ink);
  }
  .back-brand__dot {
    width: 20px;
    height: 20px;
    border-radius: 50%;
    background: var(--ink);
  }
  .back-brand__name {
    font-weight: 600;
    font-size: 18px;
  }
  .holder {
    position: absolute;
    left: 46px;
    top: 118px;
  }
  .holder__name {
    font-weight: 600;
    font-size: 28px;
    line-height: 1;
    letter-spacing: 0.3px;
    text-transform: uppercase;
    background: linear-gradient(90deg, var(--navy), var(--cyan));
    -webkit-background-clip: text;
    background-clip: text;
    color: transparent;
  }
  .holder__title {
    margin-top: 4px;
    font-weight: 600;
    font-size: 19px;
    color: var(--ink);
  }
  .contact {
    position: absolute;
    left: 46px;
    top: 246px;
    list-style: none;
    font-weight: 500;
    font-size: 14.5px;
    line-height: 18px;
    color: var(--ink);
  }
</style>
</head>
<body>
  <main class="canvas">
    <section class="card card--front" aria-label="Card front">
      <div class="front-brand">
        <span class="front-brand__dot"></span>
        <span class="front-brand__name">Corvana Wound Care</span>
      </div>
    </section>

    <section class="card card--back" aria-label="Card back">
      <div class="back-brand">
        <span class="back-brand__dot"></span>
        <span class="back-brand__name">Corvana Wound Care</span>
      </div>
      <div class="holder">
        <h1 class="holder__name">Daniel Harrowe</h1>
        <p class="holder__title">Managing Director</p>
      </div>
      <ul class="contact">
        <li class="contact__email">d.harrowe@corvana.com</li>
        <li class="contact__phone">555 014 27 80</li>
      </ul>
    </section>
  </main>
</body>
</html>
```